Martin Halvorsen Pianist Teacher Examiner

I need a website design to promote my business as a professional classical pianist and a piano teacher of all levels.
I want it to look a mixture of old world opulence (eg antique grand piano?) and modern text. It should have an elegant, beautiful and relaxing feel.

Industry/Entity Type

Teacher

```html
<!DOCTYPE html>
<html lang="en">
<head>
<meta charset="utf-8">
<title>Martin Halvorsen – Professional Piano Teacher</title>
<link rel="stylesheet" href="https://fonts.googleapis.com/css2?family=Marcellus+SC&family=Source+Sans+3:wght@400&display=swap">
<style>
  :root {
    --green: #3ab54a;
    --ink: #111111;
    --paper: #ffffff;
    --photo-dark: #2e2e30;
    --photo-mid: #55524e;
    --keys-dark: #1c1c1c;
    --keys-light: #d9d9d9;
  }
  * { margin: 0; padding: 0; box-sizing: border-box; }
  html, body {
    width: 1200px;
    height: 1000px;
    overflow: hidden;
    background: var(--paper);
    color: var(--ink);
  }
  .page {
    position: relative;
    width: 1200px;
    height: 1000px;
  }
  .top-band {
    position: absolute;
    left: 51px; top: 26px;
    width: 1092px; height: 34px;
    background: var(--green);
  }
  .main-nav {
    position: absolute;
    left: 0; top: 80px;
    width: 1200px; height: 40px;
    font-family: "Marcellus SC", serif;
    font-size: 30px;
    letter-spacing: 2px;
    color: var(--ink);
  }
  .main-nav a {
    position: absolute;
    top: 0;
    color: inherit;
    text-decoration: none;
    text-transform: uppercase;
    line-height: 40px;
  }
  .nav-home { left: 54px; }
  .nav-biography { left: 203px; }
  .nav-lessons { left: 443px; }
  .nav-students { left: 620px; }
  .nav-policy { left: 833px; }
  .nav-contact { left: 990px; top: 5px !important; }

  .hero {
    position: absolute;
    left: 51px; top: 138px;
    width: 1097px; height: 257px;
    background: var(--green);
  }
  .hero-tagline {
    position: absolute;
    right: 42px; top: 44px;
    font-family: "Marcellus SC", serif;
    font-weight: 400;
    font-size: 44px;
    letter-spacing: 2px;
    line-height: 56px;
    white-space: nowrap;
  }
  .hero-name {
    position: absolute;
    right: 66px; top: 118px;
    font-family: "Source Sans 3", sans-serif;
    font-weight: 400;
    font-size: 66px;
    line-height: 80px;
    white-space: nowrap;
  }
  .portrait {
    position: absolute;
    left: 97px; top: 302px;
    width: 289px; height: 434px;
    background: linear-gradient(160deg, var(--photo-dark) 0%, #3a3938 55%, var(--photo-mid) 100%);
  }
  .intro {
    position: absolute;
    left: 500px; top: 468px;
    width: 644px;
    font-family: "Source Sans 3", sans-serif;
    font-size: 19.5px;
    line-height: 27.2px;
    text-align: justify;
    color: var(--ink);
  }
  .intro-lead { font-size: 26px; }
  .keyboard-band {
    position: absolute;
    left: 0; top: 796px;
    width: 1200px; height: 142px;
    background: linear-gradient(180deg, var(--keys-dark) 0%, #2a2a2a 40%, #6d6d6d 55%, var(--keys-light) 75%, #a8a8a8 92%, var(--keys-dark) 100%);
  }
  .site-footer {
    position: absolute;
    left: 51px; top: 940px;
    width: 1092px; height: 33px;
    background: var(--green);
    font-family: "Source Sans 3", sans-serif;
    font-size: 19px;
    line-height: 33px;
    padding-left: 14px;
  }
</style>
</head>
<body>
<div class="page">
  <div class="top-band"></div>

  <nav class="main-nav">
    <a class="nav-home" href="#">Home</a>
    <a class="nav-biography" href="#">Biography</a>
    <a class="nav-lessons" href="#">Lessons</a>
    <a class="nav-students" href="#">Students</a>
    <a class="nav-policy" href="#">Policy</a>
    <a class="nav-contact" href="#">Contact</a>
  </nav>

  <header class="hero">
    <h2 class="hero-tagline">Professional piano teacher</h2>
    <h1 class="hero-name">Martin Halvorsen</h1>
  </header>

  <div class="portrait" role="img" aria-label="Portrait of the pianist kneeling beside a small white piano against a dark studio backdrop"></div>

  <p class="intro"><span class="intro-lead">Lorem ipsum</span> dolor sit amet, consectetur adipsing elit. Curabitur accumsan tristique nibh eget feugiat. Donec tellus massa, euismod quis sem non, aliquam tempus est. In vel nunc in ipsum commodo rutrum vel eu mi. Quisque nec sodales arcu. In feugiat blandit eros ac blandit. Donec porttitor libero feugiat tortor dapibus bibendum. Nunc tincidunt metus non magna condimentum laoreet id sit amet dolor. Nunc est purus, elementum non tortor eget, cursus aliquam</p>

  <div class="keyboard-band" role="img" aria-label="Black and white photograph of an antique piano keyboard"></div>

  <footer class="site-footer">©2014 Martin Halvorsen. All right reserved</footer>
</div>
</body>
</html>
```